Cedar Row Maintenance and Concierge Flyer

We need a flyer for cedar row maintenance and concierge service. We specialize in and provide residential maintenance and errand services to retired and semi retired persons living in the Lake Norman area. The services we include:
Lighting and plumbing repairs
Ceiling fan installation
Handicap accessories
Locks and security
Picture hanging
Hang blinds
Furniture arrangement / assembly
Pressure washing
Battery Jump start
and more...

Our Concierge services include:
Errand running
Grocery shopping
Wellness Checks
Dog Walk
Garbage Collection
and more...

We offer monthly service agreements and 24/7 access
Call text or e-mail for more information
704.555.0187
1cedarrowmaint@quillpostmail.com

The design should invoke a sense of trust and a customer service driven mission

Target Market(s)

Residential maintenance

Industry/Entity Type

Property Maintenance

Contact Information for Business Card

Derek Halvorsen
48176 Quimby Ferrel Rd.
Cornelius NC 28031
704.555.0187
with uploaded logo

Requirements
Nice to have
• Would like a postcard size flyer. Front and back
Should not have
• No pics of of people wearing hard hats or pics of blueprints. No pics of commercial or industrial maintenance.

```html
<!DOCTYPE html>
<html lang="en">
<head>
<meta charset="utf-8">
<title>Cedar Row Maintenance and Concierge</title>
<link rel="stylesheet" href="https://fonts.googleapis.com/css2?family=Montserrat:wght@300;400;500;600;800&family=Source+Sans+3:wght@400;500&display=swap">
<style>
  :root {
    --red: #e01e26;
    --red-deep: #c8141c;
    --ink: #1d1d1d;
    --grey-text: #5a5a5a;
    --grey-light: #e4e4e4;
    --grey-mid: #a9a9a9;
    --grey-dark: #5b5b5b;
    --road: #050505;
    --paper: #ffffff;
  }
  * { margin: 0; padding: 0; box-sizing: border-box; }
  html, body { width: 1200px; height: 869px; overflow: hidden; background: var(--paper); }
  .flyer {
    position: relative;
    width: 1200px;
    height: 869px;
    background: var(--paper);
    font-family: "Montserrat", sans-serif;
    color: var(--ink);
  }
  .streetscape { position: absolute; left: 0; top: 0; width: 1200px; height: 440px; }
  .brand {
    position: absolute;
    left: 360px;
    top: 88px;
    display: flex;
    align-items: center;
    gap: 18px;
  }
  .brand-mark {
    width: 84px; height: 84px;
    border-radius: 50%;
    background: var(--red);
    flex: none;
  }
  .brand-name {
    font-family: "Montserrat", sans-serif;
    font-weight: 500;
    color: var(--grey-text);
    font-size: 29px;
    line-height: 1.2;
    letter-spacing: 0.5px;
  }
  .mission {
    position: absolute;
    left: 300px;
    top: 230px;
    width: 590px;
    text-align: center;
    color: var(--paper);
    font-weight: 600;
    font-size: 25px;
    line-height: 32px;
    white-space: nowrap;
  }
  .service-list-block { position: absolute; }
  .service-list-block h2 {
    color: var(--red);
    font-weight: 500;
    font-size: 30px;
    line-height: 36px;
  }
  .service-list-block ul { list-style: none; }
  .service-list-block li {
    font-weight: 400;
    font-size: 21px;
    line-height: 27.5px;
    color: #2a2a2a;
    padding-left: 16px;
    position: relative;
  }
  .service-list-block li::before {
    content: "";
    position: absolute;
    left: 2px; top: 12px;
    width: 5px; height: 5px;
    border-radius: 50%;
    background: var(--red);
  }
  .service-list-block .more {
    font-size: 21px;
    line-height: 27.5px;
    margin-top: 8px;
    color: #2a2a2a;
  }
  .maintenance { left: 64px; top: 455px; }
  .concierge { left: 607px; top: 451px; }
  .team {
    position: absolute;
    left: 410px; top: 702px;
    width: 194px; height: 122px;
    background: var(--red);
    border-radius: 48px 48px 10px 10px;
    opacity: 0.9;
  }
  .contact {
    position: absolute;
    left: 612px; top: 700px;
    width: 540px;
    text-align: center;
    font-family: "Source Sans 3", sans-serif;
  }
  .contact .offer { font-size: 20.5px; line-height: 28px; color: var(--ink); }
  .contact .call { font-size: 24.5px; line-height: 34px; color: var(--ink); font-weight: 500; }
  .contact .phone {
    font-family: "Montserrat", sans-serif;
    font-weight: 800;
    color: var(--red);
    font-size: 31px;
    line-height: 38px;
  }
  .contact .email { font-size: 16px; line-height: 22px; color: var(--ink); }
</style>
</head>
<body>
<main class="flyer">
  <svg class="streetscape" viewBox="0 0 1200 440" xmlns="http://www.w3.org/2000/svg">
    <defs>
      <linearGradient id="missionFill" x1="0" y1="0" x2="0" y2="1">
        <stop offset="0" stop-color="#ffffff"/>
        <stop offset="0.16" stop-color="#ef2b32"/>
        <stop offset="1" stop-color="#c4141b"/>
      </linearGradient>
      <linearGradient id="townFill" x1="0" y1="0" x2="0" y2="1">
        <stop offset="0" stop-color="#8c8c8c"/>
        <stop offset="0.55" stop-color="#a8a8a8"/>
        <stop offset="1" stop-color="#e4e4e4"/>
      </linearGradient>
    </defs>
    <rect class="ground" x="21" y="250" width="1153" height="117" fill="var(--grey-light)"/>
    <rect class="town-left" role="img" aria-label="Grey row houses and trees along the street" x="21" y="27" width="281" height="330" rx="2" fill="url(#townFill)"/>
    <rect class="town-right" role="img" aria-label="Grey row houses and trees along the street" x="869" y="31" width="305" height="326" rx="2" fill="url(#townFill)"/>
    <polygon class="mission-band" points="338,210 849,210 1042,365 152,365" fill="url(#missionFill)"/>
    <rect class="curb" x="27" y="367" width="1153" height="10" fill="var(--grey-mid)"/>
    <rect class="road" x="21" y="379" width="1153" height="49" fill="var(--road)"/>
    <line x1="21" y1="401" x2="1174" y2="401" stroke="#bdbdbd" stroke-width="2"/>
    <line x1="36" y1="410" x2="1174" y2="410" stroke="#ffffff" stroke-width="3" stroke-dasharray="8 49"/>
  </svg>

  <div class="brand">
    <span class="brand-mark"></span>
    <div class="brand-name">Cedar Row<br>Maintenance &amp; Concierge</div>
  </div>

  <p class="mission">We specialize in and provide<br>residential maintenance and errand<br>services to retired and semi retired<br>persons living in the Lake Norman area.</p>

  <section class="service-list-block maintenance">
    <h2>The services we include:</h2>
    <ul>
      <li>Lighting and plumbing repairs</li>
      <li>Ceiling fan installation</li>
      <li>Handicap accessories</li>
      <li>Locks and security</li>
      <li>Picture hanging</li>
      <li>Hang blinds</li>
      <li>Furniture arrangement / assembly</li>
      <li>Pressure washing</li>
      <li>Battery Jump start</li>
    </ul>
    <p class="more">and more...</p>
  </section>

  <section class="service-list-block concierge">
    <h2>Our Concierge services include:</h2>
    <ul>
      <li>Errand running</li>
      <li>Grocery shopping</li>
      <li>Wellness Checks</li>
      <li>Dog Walk</li>
      <li>Garbage Collection</li>
    </ul>
    <p class="more">and more...</p>
  </section>

  <div class="team" role="img" aria-label="Red silhouettes of a friendly service team standing together"></div>

  <section class="contact">
    <p class="offer">We offer monthly service agreements and 24/7 access</p>
    <p class="call">Call text or e-mail for more information</p>
    <p class="phone">704.555.0187</p>
    <p class="email">1cedarrowmaint@quillpostmail.com</p>
  </section>
</main>
</body>
</html>
```